Business Card Design Project

Hello
I want a Simple Business card that uses the company logo that is easily reasonable but looks professional as I am an IT Services company and would look to share these cards with prospective clients.
The details are:
Kelvo Ridge Solutions
14 Marlow Crescent
Birmingham
B7 4QT
Telephone 0845 271 6049
I would like my name Gareth Wilcombe and my title Director on the card.
Target Market(s)
IT Professionals
Industry/Entity Type
Business

```html
<!DOCTYPE html>
<html lang="en">
<head>
<meta charset="utf-8">
<title>Kelvo Ridge Solutions – Business Card</title>
<link rel="stylesheet" href="https://fonts.googleapis.com/css2?family=Questrial&display=swap">
<style>
  :root {
    --backdrop: #2b2b2b;
    --card-white: #ffffff;
    --card-black: #231f20;
    --brand-green: #6cb56c;
    --brand-yellow: #fdd35f;
    --ink: #1c1c1c;
    --light-text: #f2f2f2;
  }
  html, body {
    margin: 0;
    width: 1200px;
    height: 1000px;
    overflow: hidden;
    background: var(--backdrop);
    font-family: "Questrial", "Century Gothic", sans-serif;
  }
  .business-card {
    position: absolute;
    left: 150px;
    top: 243px;
    width: 900px;
    height: 514px;
    background: var(--card-white);
    overflow: hidden;
    box-shadow: 0 10px 30px rgba(0,0,0,0.45);
  }
  .card-waves {
    position: absolute;
    inset: 0;
    width: 900px;
    height: 514px;
  }
  .wave-black { fill: var(--card-black); }
  .wave-green { fill: var(--brand-green); }
  .wave-yellow { fill: var(--brand-yellow); }
  .wave-gap { fill: var(--card-white); }

  .holder {
    position: absolute;
    right: 60px;
    top: 42px;
    text-align: right;
  }
  .holder-name {
    font-size: 30px;
    color: var(--ink);
    letter-spacing: 1px;
    margin: 0;
    line-height: 1.1;
  }
  .holder-title {
    font-size: 18px;
    color: var(--brand-green);
    margin: 2px 0 0;
  }

  .brand {
    position: absolute;
    left: 70px;
    top: 222px;
    display: flex;
    align-items: center;
    gap: 16px;
  }
  .brand-dot {
    width: 40px;
    height: 40px;
    border-radius: 50%;
    background: var(--brand-green);
  }
  .brand-name {
    font-size: 40px;
    color: var(--ink);
    letter-spacing: 0.5px;
  }

  .contact {
    position: absolute;
    right: 40px;
    top: 262px;
    text-align: right;
    font-size: 19px;
    line-height: 27px;
    color: var(--light-text);
  }
  .contact p { margin: 0; }
  .contact-label { color: var(--brand-yellow); }
  .contact-company { color: var(--brand-green); }
</style>
</head>
<body>
  <div class="business-card">
    <svg class="card-waves" viewBox="0 0 900 514" aria-hidden="true">
      <path class="wave-yellow" d="M540 280 C 640 180, 760 110, 900 85 L900 115 C 770 135, 650 200, 540 280 Z"/>
      <path class="wave-green" d="M0 418 C 250 410, 420 390, 520 290 C 620 190, 740 140, 900 120 L900 514 L0 514 Z"/>
      <path class="wave-gap" d="M0 428 C 250 418, 425 398, 525 298 C 625 198, 745 152, 900 136 L900 514 L0 514 Z"/>
      <path class="wave-black" d="M0 436 C 250 428, 430 410, 530 310 C 630 210, 750 166, 900 150 L900 514 L0 514 Z"/>
    </svg>

    <div class="holder">
      <p class="holder-name">Gareth Wilcombe</p>
      <p class="holder-title">Director</p>
    </div>

    <div class="brand">
      <span class="brand-dot"></span>
      <span class="brand-name">Kelvo Ridge Solutions</span>
    </div>

    <div class="contact">
      <p><span class="contact-label">[T]:</span> 0845 271 6049</p>
      <p class="contact-company">Kelvo Ridge Solutions</p>
      <p>14 Marlow Crescent, Birmingham</p>
      <p>B7 4QT</p>
    </div>
  </div>
</body>
</html>
```